A new Brochure from a combination of two

We have a medical supply business and a brighter by noon companion business. I have attached a brochure from each. In the medical equipment business, I have closed the Wilmington location. So I want that taken off. There is also wasted space on the back. I maybe would like to keep the main insurances we take, but use the space from the removal of the Wilmington store, and most of the room on the back to advertise our brighter by noon business. Again, I will enclose both brochures.

```html
<!DOCTYPE html>
<html lang="en">
<head>
<meta charset="utf-8">
<title>Maple Drug &amp; Brighter by Noon – Tri-fold Brochure</title>
<link rel="stylesheet" href="https://fonts.googleapis.com/css2?family=Zilla+Slab:ital,wght@0,500;0,700;1,500;1,600&family=Tinos:ital,wght@0,400;0,700;1,400&display=swap">
<style>
:root{
  --magenta:#ad1456;
  --magenta-deep:#a3124f;
  --purple:#3c1178;
  --purple-text:#3a1c7a;
  --ink:#2b2b2b;
  --soft:#555;
  --paper:#ffffff;
  --backdrop:#e4e4e4;
  --icon-grey:#8e8e8e;
}
*{box-sizing:border-box;margin:0;padding:0}
html,body{width:1200px;height:3000px;overflow:hidden;background:var(--backdrop)}
body{font-family:"Tinos",serif;color:var(--ink);position:relative}
.spread{position:absolute;left:30px;width:1140px;height:806px;background:var(--paper);overflow:hidden;box-shadow:0 4px 18px rgba(0,0,0,.12)}
.spread--outside{top:100px}
.spread--inside{top:980px}
.shapes{position:absolute;inset:0}
.abs{position:absolute}
.photo{position:absolute}

/* outside – product panel */
.product-title{font-family:"Zilla Slab",serif;font-weight:700;font-size:18px;letter-spacing:.5px;color:#1b1b1b}
.product-text{font-size:11.5px;line-height:1.3;color:var(--ink);width:260px;margin-top:6px}
.product-photo{border-radius:6px;background:linear-gradient(135deg,#f4f4f6,#d9dde4)}

/* outside – locations */
.store-photo{background:linear-gradient(180deg,#b8c4d2 0%,#8e9aa8 55%,#6f6f6f 100%)}
.store-photo--b{background:linear-gradient(180deg,#c9d6e3 0%,#c0584a 45%,#8a8a8a 100%)}
.store-info{font-size:10px;line-height:1.3;color:var(--ink)}
.store-name{color:#d3202e;font-weight:700}

/* outside – magenta panel */
.emergency{width:380px;text-align:center;color:#fff}
.emergency .lead{font-size:13px;line-height:1.25}
.emergency .hotline-label{font-family:"Zilla Slab",serif;font-weight:700;font-size:17px;line-height:1.15;margin-top:18px;letter-spacing:.3px}
.emergency .hotline{font-family:"Zilla Slab",serif;font-weight:700;font-size:34px;margin-top:6px;letter-spacing:1px}
.emergency .ins-head{font-size:13px;line-height:1.25;margin-top:10px}
.emergency .ins-list{font-size:10px;line-height:1.3;margin-top:7px}
.emergency .note{font-size:10.5px;line-height:1.3;margin-top:12px}

/* outside – cover */
.brand{font-family:"Zilla Slab",serif;font-weight:700;color:var(--purple-text);display:flex;align-items:center;gap:8px}
.brand-mark{width:20px;height:20px;border-radius:50%;background:var(--purple)}
.brand--drug{font-size:17px;line-height:1.05}
.brand--care{font-size:21px;line-height:1.05;color:var(--purple-text);text-align:right}
.cover-title{width:378px;text-align:center;color:#fff;font-family:"Zilla Slab",serif;font-weight:700;font-size:44px;line-height:1.15}
.cover-tag{width:378px;text-align:center;color:#fff;font-family:"Zilla Slab",serif;font-style:italic;font-weight:600;font-size:18px;line-height:1.35}

/* inside */
.panel{position:absolute;top:0;width:380px;padding:0 38px}
.h-purple{font-family:"Zilla Slab",serif;font-weight:700;font-size:32px;color:var(--purple-text);line-height:1}
.h-magenta{font-family:"Zilla Slab",serif;font-weight:700;font-size:30px;color:var(--magenta);line-height:1.05}
.h-sub{font-family:"Zilla Slab",serif;font-weight:700;font-size:16px;color:var(--purple-text)}
.h-sub--magenta{color:var(--magenta);font-size:20px}
.copy{font-size:10px;line-height:1.32;color:var(--soft)}
.copy p+p{margin-top:6px}
.services{display:grid;grid-template-columns:1fr 1fr;row-gap:12px;column-gap:8px;margin-top:10px}
.service{display:flex;align-items:center;gap:8px;font-size:9.5px;line-height:1.2;color:var(--soft)}
.service-icon{flex:0 0 22px;height:22px;border-radius:50%;background:var(--icon-grey);position:relative}
.service-icon::after{content:"";position:absolute;inset:6px;border-radius:50%;border:1.5px solid #fff}
.testimonial{position:absolute;left:38px;top:590px;width:297px;height:172px;border:2px solid var(--purple);padding:22px 14px 10px 22px;font-size:8.5px;line-height:1.3;color:var(--ink)}
.testimonial p+p{margin-top:8px}
.quote-mark{position:absolute;left:-6px;top:-40px;font-family:"Zilla Slab",serif;font-weight:700;font-size:72px;color:var(--magenta);background:var(--paper);padding:0 4px;line-height:1}
.checklist{list-style:none;display:grid;grid-template-columns:1fr 1fr;column-gap:10px;row-gap:3px;font-size:9.5px;color:var(--soft);line-height:1.2}
.checklist li{position:relative;padding-left:14px}
.checklist li::before{content:"";position:absolute;left:0;top:1px;width:8px;height:8px;border:1px solid var(--magenta)}
.checklist li::after{content:"";position:absolute;left:2px;top:2px;width:5px;height:3px;border-left:1.5px solid var(--magenta);border-bottom:1.5px solid var(--magenta);transform:rotate(-45deg)}
.unique-head{font-family:"Zilla Slab",serif;font-weight:700;font-size:30px;line-height:1.15;color:#fff;text-align:right}
.unique-item{display:flex;gap:14px;align-items:flex-start}
.unique-icon{flex:0 0 36px;height:36px;border-radius:50%;background:var(--magenta);position:relative}
.unique-icon::after{content:"";position:absolute;inset:8px;border-radius:50%;border:2px solid #fff}
.unique-title{font-family:"Zilla Slab",serif;font-weight:700;font-size:13px;color:var(--magenta)}
.unique-text{font-size:9.5px;color:var(--soft);margin-top:5px}
.checklist--unique{grid-template-columns:auto auto;column-gap:14px;row-gap:10px;font-size:8.5px}
</style>
</head>
<body>

<!-- ============ OUTSIDE ============ -->
<section class="spread spread--outside">
  <svg class="shapes" width="1140" height="806" viewBox="0 0 1140 806" aria-hidden="true">
    <polygon points="377,396 762,285 955,182 1140,262 1140,806 377,806" fill="var(--magenta-deep)"/>
  </svg>

  <svg class="photo" style="left:0;top:0" width="1140" height="806" viewBox="0 0 1140 806" role="img" aria-label="Photo of a smiling older man with a small white dog and a woman embracing him">
    <defs><linearGradient id="coverPhoto" x1="0" y1="0" x2="1" y2="1"><stop offset="0" stop-color="#e9ddd6"/><stop offset="1" stop-color="#b79b8f"/></linearGradient></defs>
    <polygon points="774,320 955,215 1140,305 1140,806 774,806" fill="url(#coverPhoto)"/>
  </svg>

  <svg class="shapes" width="1140" height="806" viewBox="0 0 1140 806" aria-hidden="true">
    <polygon points="762,555 955,500 1140,548 1140,806 762,806" fill="var(--purple)"/>
  </svg>

  <!-- product panel -->
  <div class="abs" style="left:34px;top:62px">
    <div class="product-title">RESPIRATORY CARE</div>
    <div class="product-text">We work with you and your providers to ensure proper treatment for your medical needs.</div>
  </div>
  <div class="photo product-photo" role="img" aria-label="Nebulizer machine with mask" style="left:88px;top:150px;width:160px;height:120px"></div>

  <div class="abs" style="left:34px;top:272px">
    <div class="product-title">SLEEP APNEA THERAPY</div>
    <div class="product-text">Our licensed Respiratory Care Practitioner takes the time to make sure you have the most current technology, equipment and fit to receive the best results.</div>
  </div>
  <div class="photo product-photo" role="img" aria-label="CPAP machine with hose" style="left:128px;top:385px;width:120px;height:110px"></div>

  <div class="abs" style="left:34px;top:537px">
    <div class="product-title">HOME OXYGEN THERAPY</div>
    <div class="product-text">Equipment and supplies are delivered by trained Technicians. They also assist in your training on correct use and maintenance of your home use and portable system.</div>
  </div>

  <div class="abs" style="left:34px;top:676px">
    <div class="product-title">BREAST PUMP RENTALS &amp; SALES</div>
    <div class="product-text">Specially trained members of our staff will help you decide which model is best suited for your needs.</div>
  </div>

  <!-- locations -->
  <div class="photo store-photo" role="img" aria-label="Storefront of the Pinecrest location" style="left:428px;top:43px;width:134px;height:104px"></div>
  <div class="photo store-photo store-photo--b" role="img" aria-label="Storefront of the Oakmere location" style="left:582px;top:43px;width:134px;height:104px"></div>

  <div class="abs store-info" style="left:428px;top:158px;width:150px">
    <div class="store-name">Pinecrest-<br>Harbor Mill Street</div>
    <div>520 Harbor Mill Street<br>Pinecrest<br>NC 28001</div>
    <div style="margin-top:4px">Phone: 910-555-0118<br>DME Fax: 910-555-0127</div>
    <div style="margin-top:4px">Hours :Mon-Fri<br>8:30-6:00 Closed Sat &amp; Sun</div>
  </div>
  <div class="abs store-info" style="left:582px;top:166px;width:160px">
    <div class="store-name">Oakmere</div>
    <div>Oakmere Town Center<br>4410 Coastal Hwy Suite 12<br>Oakmere, NC 28002</div>
    <div style="margin-top:4px">Phone: 910-555-0163<br>Pharmacy Fax: 910-555-0179</div>
    <div style="margin-top:4px">Hours Mon-Fri<br>9:00-7:00 Sat 9:00-2:00<br>Sun-Closed</div>
  </div>

  <!-- emergency / insurance -->
  <div class="abs emergency" style="left:382px;top:398px">
    <div class="lead">Locally Owned &amp; Operated Servicing<br>Eastern North Carolina</div>
    <div class="hotline-label">24 HOUR EMERGENCY<br>SERVICE</div>
    <div class="hotline">888-555-0142</div>
    <div class="ins-head">Insurance<br>Preferred Providers for:</div>
    <div class="ins-list">Shieldcare/StatePlan/Medway<br>Azure Cross Health</div>
    <div class="ins-head">Medicare Supplements<br>&amp; Part D:</div>
    <div class="ins-list">Northstar/Covehill<br>Swift Scripts<br>Silverline Rx Choice<br>ClearviewRx Plus / Medpath<br>Keystone Therapeutics</div>
    <div class="note">We also provide billing to most private insurance<br>companies upon your request.</div>
  </div>

  <!-- cover -->
  <div class="abs brand brand--drug" style="left:800px;top:92px">
    <span class="brand-mark"></span>
    <span>Maple Drug<br>&amp; Home Medical</span>
  </div>
  <div class="abs brand brand--care" style="left:1000px;top:76px">
    <span>Brighter<br>by Noon</span>
  </div>

  <div class="abs cover-title" style="left:762px;top:590px">Quality Care<br>at Home</div>
  <div class="abs cover-tag" style="left:762px;top:705px">Giving Compassion,<br>Respect, and Independence</div>
</section>

<!-- ============ INSIDE ============ -->
<section class="spread spread--inside">
  <svg class="photo" style="left:0;top:0" width="1140" height="162" viewBox="0 0 1140 162" role="img" aria-label="Banner photo of a caregiver chatting with a senior woman and a senior on a video call with a doctor">
    <defs><linearGradient id="bannerPhoto" x1="0" y1="0" x2="1" y2="0"><stop offset="0" stop-color="#dfe3e8"/><stop offset=".5" stop-color="#cbbfb4"/><stop offset="1" stop-color="#8d8478"/></linearGradient></defs>
    <rect width="1140" height="162" fill="url(#bannerPhoto)"/>
  </svg>
  <svg class="shapes" width="1140" height="806" viewBox="0 0 1140 806" aria-hidden="true">
    <polygon points="713,162 1030,0 1140,0 1140,162" fill="var(--magenta)"/>
  </svg>

  <!-- services panel -->
  <div class="panel" style="left:0;top:176px">
    <h2 class="h-purple">Our Services</h2>
    <div class="copy" style="margin-top:10px">
      <p>Brighter by Noon is the perfect solution for seniors that need support to maintain independence in their place of residence, no matter where they call home.<br>We customize care plans that are tailored to meet each individual's unique needs. Our services are personalized, affordable and are available 7 days a week/ 24 hours a day.</p>
    </div>
    <h3 class="h-sub h-sub--magenta" style="margin-top:16px">We Can Help With:</h3>
    <div class="services">
      <div class="service"><span class="service-icon"></span>Meal Planning<br>&amp; Preparation</div>
      <div class="service"><span class="service-icon"></span>Transportation,<br>Shopping &amp; Errands</div>
      <div class="service"><span class="service-icon"></span>Light Housekeeping<br>&amp; Laundry</div>
      <div class="service"><span class="service-icon"></span>Companionship<br>&amp; Mental Stimulation</div>
      <div class="service"><span class="service-icon"></span>Medication<br>Reminders</div>
      <div class="service"><span class="service-icon"></span>Alzheimer's &amp;<br>Dementia Care</div>
      <div class="service"><span class="service-icon"></span>Respite Care</div>
      <div class="service"><span class="service-icon"></span>Long Distance Travel<br>/Relocation Assistance</div>
      <div class="service"><span class="service-icon"></span>Encouragement &amp;<br>Monitoring of Exercises</div>
    </div>
  </div>

  <blockquote class="testimonial">
    <span class="quote-mark">“</span>
    <p>The ladies who come daily are nice, friendly, and effective. They clean up daily, make my bed, fix my lunch, and make sure I take my medicines. The ladies are like friends. They are friends to my little dog who absolutely loves them. For anyone who wants or needs assistance, their service is ideal.</p>
    <p>After a fall and rehab, my 88-year-old mom desperately wanted to remain in her home as long as possible. I didn't know where to begin. I contacted Brighter by Noon and met with their Geriatric Care Manager. She quickly developed a plan to keep her home. She organized everything and was a blessing to our family.</p>
  </blockquote>

  <!-- advocacy panel -->
  <div class="panel" style="left:380px;top:178px">
    <h2 class="h-purple">Care Advocacy</h2>
    <div class="copy" style="margin-top:10px">
      <p>Our experts plan and coordinate care for the elderly to improve their quality of life and maintain independence for as long as possible.</p>
      <p>We organize the best combination of services: housing, home care services, socialization programs, financial and legal planning. Our advocates understand your loved one's needs and arrange &amp; monitor the implementation of services.</p>
    </div>
    <h2 class="h-magenta" style="margin-top:16px">In-Home Care</h2>
    <h3 class="h-sub" style="margin-top:14px">Getting Started</h3>
    <div class="copy" style="margin-top:4px">
      <p>Before starting services, we learn about your loved one's daily routines. Our team conducts a 45 minute in-home assessment that covers lifestyle, personality, established behaviors, and medical conditions. These factors guide the level of assistance necessary to help the patient remain independent in their home.</p>
    </div>
    <h3 class="h-sub" style="margin-top:12px">We Will Discuss:</h3>
    <ul class="checklist" style="margin-top:8px">
      <li>Nutrition &amp; Cooking</li><li>Ambulation &amp; Balance</li>
      <li>Health Challenges</li><li>Medical Alert Buttons</li>
      <li>Transportation Needs</li><li>Daily Routines</li>
      <li>Cleaning &amp; Home Maintenance</li><li>Memory Concerns &amp; Wandering</li>
      <li>Safety &amp; Isolation Concerns</li><li>Medication</li>
      <li></li><li>Compliance</li>
    </ul>
    <h3 class="h-sub" style="margin-top:12px">Our Caregivers</h3>
    <div class="copy" style="margin-top:4px">
      <p>We are devoted to providing the most professional, reliable and friendly caregivers in the industry. We seek mature-minded individuals with prior life experience in caring who have shown reliability and compassion. We would never hire a person that we wouldn't trust to care for our own loved ones.</p>
    </div>
  </div>

  <!-- unique panel -->
  <div class="abs unique-head" style="right:40px;top:58px">How We<br>Are Unique:</div>

  <div class="panel" style="left:760px;top:180px;padding-left:42px;padding-right:30px">
    <div class="unique-item">
      <span class="unique-icon"></span>
      <div><div class="unique-title">Continuity Of Caregivers</div><div class="unique-text">We strive to keep the same caregiver for each visit.</div></div>
    </div>
    <div class="unique-item" style="margin-top:30px">
      <span class="unique-icon"></span>
      <div><div class="unique-title">Community Connection</div><div class="unique-text">We are locally owned &amp; operated.</div></div>
    </div>
    <div class="unique-item" style="margin-top:30px">
      <span class="unique-icon"></span>
      <div><div class="unique-title">Training</div><div class="unique-text">Our continued training program leads the industry</div></div>
    </div>
    <ul class="checklist checklist--unique" style="margin-top:16px;margin-left:44px">
      <li>Fall Prevention</li><li>Senior Fraud Prevention</li>
      <li>Nutrition &amp; Cooking</li><li>Alzheimer's &amp; Dementia Care</li>
    </ul>
    <h2 class="h-magenta" style="margin-top:42px;margin-left:10px">Support In<br>Times Of Need</h2>
    <div class="copy" style="margin-top:18px;margin-left:10px">
      <p>We help navigate the complex and confusing health care system. Care advocates interact with medical professionals and service providers to ensure our clients receive quality care and are protected from those who may take advantage of the elderly.</p>
      <p>We can often help prevent a crisis before it occurs. If one does happen, we provide guidance, support and management. We act as liaisons to families, especially those living at a distance.</p>
      <p>We monitor changing needs, manage and attend medical appointments, and provide feedback to the family. If a hospitalization occurs, our care advocates are there for your loved one from admission through discharge, and safely back home.</p>
    </div>
  </div>
</section>

</body>
</html>
```